Design a Postcard app mockup

When travelling user can take a picture, add his own greeting-text and send it as a real postcard right from his mobile device. The postcard will be printed by us and delivered directly to the recipients door.
Surprise your friends with your own postcard even during your vacation or use postcards for invitations to wedding, birthdays or other parties!
Unforgettable moments - easy to capture and share.

This app design will be used in both - iOS and Android, so please keep that in mind that it has to work on phones and tablets for iOS and Android.
We need each screen for a tablet (10 inch) and phone (4.7 inch)

Please see the attached wireframes we have developed:

Step 1: Splash screens; - 3 screens (please see in the attached wireframes the screens we would like you to make - they're with a red outline)
(info about the app);

Step 2: Postcard order process: - 7 screens (please see in the attached wireframes the screens we would like you to make - they're with a red outline)
1. Make or select 1 Photo;
2. Add customized text;
3. Select a recipient;
4. Payment process;

Step 3: Projects menu; - 1 screen (please see in the attached wireframes the screens we would like you to make - they're with a red outline)
(see your unfinished postcards)

Step 4: Main menu: - 1 screen (please see in the attached wireframes the screens we would like you to make - they're with a red outline)
1. about;
2. settings;
3. support;
4. contacts;
5. privacy policy

The Logo of the app will be placed by us in the final version. Until then please keep in mind that the background color for the logo is #CC071E and the logo font color will be #6D6E71. The design of the app must be clean, modern looking and all icons should be easy to understand.

```html
<!DOCTYPE html>
<html lang="en">
<head>
<meta charset="utf-8">
<title>Home</title>
<link rel="stylesheet" href="https://fonts.googleapis.com/css2?family=Fira+Sans:wght@400&family=Raleway:wght@200;300&display=swap">
<style>
  :root {
    --brand-red: #cc071e;
    --tab-divider: #d9364a;
    --tab-muted: #8c0616;
    --tile-camera: #dc0c27;
    --tile-gallery: #e8122a;
    --tile-photonest: #ef0b26;
    --tile-friendspace: #e0071e;
    --white: #ffffff;
  }
  * { box-sizing: border-box; margin: 0; padding: 0; }
  html, body { width: 676px; height: 1200px; overflow: hidden; background: var(--brand-red); }
  .screen {
    position: relative; width: 676px; height: 1200px; overflow: hidden;
    background: var(--brand-red); color: var(--white);
    font-family: "Fira Sans", sans-serif;
  }
  .top-bar { position: absolute; left: 0; top: 0; width: 676px; height: 84px; }
  .menu-button { position: absolute; left: 32px; top: 28px; width: 36px; height: 26px; }
  .menu-button span {
    position: absolute; left: 0; width: 36px; height: 5px; border-radius: 3px; background: var(--white);
  }
  .menu-button span:nth-child(1) { top: 0; }
  .menu-button span:nth-child(2) { top: 10px; }
  .menu-button span:nth-child(3) { top: 20px; }
  .screen-title {
    position: absolute; left: 0; right: 0; top: 20px; text-align: center;
    font-family: "Raleway", sans-serif; font-weight: 300; font-size: 36px; letter-spacing: 1px;
  }
  .brand-mark {
    position: absolute; left: 0; right: 0; top: 230px; height: 124px;
    display: flex; align-items: center; justify-content: center; gap: 32px;
  }
  .brand-mark .mark-square {
    width: 120px; height: 120px; border: 6px solid var(--white);
  }
  .brand-mark .brand-name {
    font-family: "Fira Sans", sans-serif; font-weight: 400; font-size: 48px; letter-spacing: 2px;
  }
  .tab-bar {
    position: absolute; left: 0; top: 530px; width: 676px; height: 80px;
    border-top: 1px solid var(--tab-divider); border-bottom: 1px solid var(--tab-divider);
    display: flex;
  }
  .tab {
    position: relative; flex: 1; display: flex; align-items: center; justify-content: center;
    font-size: 25px;
  }
  .tab + .tab::before {
    content: ""; position: absolute; left: 0; top: 6px; bottom: 6px; width: 1px; background: var(--tab-divider);
  }
  .tab.is-active::after {
    content: ""; position: absolute; left: 42px; right: 41px; bottom: -1px; height: 3px; background: var(--white);
  }
  .tab.is-muted { color: var(--tab-muted); }
  .source-grid {
    position: absolute; left: 0; top: 610px; width: 676px; height: 590px;
    display: grid; grid-template-columns: 337px 339px; grid-template-rows: 295px 295px;
  }
  .source-tile {
    display: flex; flex-direction: column; align-items: center; justify-content: flex-start;
    padding-top: 56px; text-align: center; font-size: 25px; line-height: 34px;
  }
  .source-tile .tile-icon { width: 90px; height: 90px; margin-bottom: 16px; }
  .tile-camera { background: var(--tile-camera); }
  .tile-gallery { background: var(--tile-gallery); }
  .tile-photonest { background: var(--tile-photonest); }
  .tile-friendspace { background: var(--tile-friendspace); }
  .plain-badge { width: 74px; height: 74px; margin: 8px 0 24px; border: 5px solid var(--white); }
  .plain-badge.round { border-radius: 50%; }
</style>
</head>
<body>
<main class="screen">
  <header class="top-bar">
    <div class="menu-button" aria-label="Menu"><span></span><span></span><span></span></div>
    <h1 class="screen-title">HOME</h1>
  </header>

  <section class="brand-mark">
    <div class="mark-square"></div>
    <div class="brand-name">POSTCARD</div>
  </section>

  <nav class="tab-bar">
    <div class="tab is-active">POSTCARD</div>
    <div class="tab is-muted">PROJECT</div>
  </nav>

  <section class="source-grid">
    <div class="source-tile tile-camera">
      <svg class="tile-icon" viewBox="0 0 90 90" fill="none" stroke="#fff" stroke-width="5" stroke-linejoin="round">
        <path d="M6 26h20l8-10h22l8 10h20v50H6z"/>
        <circle cx="45" cy="50" r="15"/>
      </svg>
      <p>Take a new<br>picture</p>
    </div>
    <div class="source-tile tile-gallery">
      <svg class="tile-icon" viewBox="0 0 90 90" fill="none" stroke="#fff" stroke-width="5" stroke-linejoin="round">
        <rect x="8" y="16" width="76" height="58"/>
        <path d="M14 64l22-22 14 14 10-10 18 18"/>
        <circle cx="62" cy="32" r="6"/>
      </svg>
      <p>Select from<br>Gallery</p>
    </div>
    <div class="source-tile tile-photonest">
      <div class="plain-badge"></div>
      <p>Get your<br>Photonest picture</p>
    </div>
    <div class="source-tile tile-friendspace">
      <div class="plain-badge round"></div>
      <p>Get your<br>Friendspace picture</p>
    </div>
  </section>
</main>
</body>
</html>
```